Beekeeper needs box/label design for honey/CBD and other honey-related products

We need a box (or label) design for a beekeeping company in Virginia called Tamsin Hollow Farm. Our products will include honey mixed with CBD oil and other essential oils (vanilla, lavender, etc).The box design should be scalable to include several different honey/oil products. We would like to incorporate our current farm logo into the design. Here is a link to a honey producing company with a series of products using their honey mixed with certain oils. It's a good reference of what type box/label design we would like (https://corbinandlyle.co/pages/honey).

Target Market(s)

Retail stores and consumers

Requirements
Must have
• Tamsin Hollow Farm name and logo

```html
<!DOCTYPE html>
<html lang="en">
<head>
<meta charset="UTF-8">
<title>Tamsin Hollow Farm – Hemp-Infused Honey Label</title>
<link rel="stylesheet" href="https://fonts.googleapis.com/css2?family=Cinzel:wght@400;500&family=Montserrat:wght@300;400;600&display=swap">
<style>
  :root {
    --page-bg: #ececec;
    --label-light: #ebedda;
    --label-mid: #dfe2c4;
    --label-edge: #d3d7b4;
    --leaf-green: #8a9040;
    --ink: #2c2b28;
    --ink-soft: #6e6d66;
    --pattern-tone: rgba(176, 182, 138, 0.28);
  }
  * { box-sizing: border-box; margin: 0; padding: 0; }
  html, body {
    width: 1200px; height: 960px; overflow: hidden;
    background: var(--page-bg);
  }
  .label {
    position: absolute; left: 290px; top: 98px;
    width: 620px; height: 765px;
    background: linear-gradient(90deg, var(--label-edge) 0%, var(--label-light) 22%, var(--label-mid) 60%, var(--label-edge) 100%);
    font-family: "Montserrat", sans-serif;
    color: var(--ink);
    overflow: hidden;
  }
  .background-pattern {
    position: absolute; left: 0; top: 285px; width: 620px; height: 450px;
    background: linear-gradient(180deg, transparent 0%, var(--pattern-tone) 30%, var(--pattern-tone) 70%, transparent 100%);
  }
  .product-type {
    position: absolute; left: 30px; top: 100px;
    font-size: 19px; font-weight: 300; color: var(--ink-soft); letter-spacing: 0.5px;
  }
  .product-name {
    position: absolute; left: 29px; top: 128px;
    font-size: 38px; font-weight: 600; letter-spacing: 5px; color: #3e3d39;
  }
  .farm-mark {
    position: absolute; left: 462px; top: 62px; width: 108px;
    display: flex; flex-direction: column; align-items: center; gap: 6px;
  }
  .farm-mark-square {
    width: 60px; height: 60px; border: 4px solid var(--leaf-green);
  }
  .farm-mark-name {
    font-size: 11px; font-weight: 600; color: var(--leaf-green); text-align: center; line-height: 1.3;
  }
  .top-rule {
    position: absolute; left: 12px; top: 188px; width: 592px; height: 2px; background: var(--leaf-green);
  }
  .flavour {
    position: absolute; left: 30px; top: 203px;
    font-size: 15px; font-weight: 600; letter-spacing: 6.5px; color: var(--leaf-green);
  }
  .brand-name {
    position: absolute; left: 0; top: 318px; width: 620px; text-align: center;
    font-family: "Cinzel", serif; font-weight: 400; font-size: 92px; line-height: 1;
    color: var(--ink); letter-spacing: 0;
  }
  .brand-sub {
    position: absolute; left: 0; top: 455px; width: 620px; text-align: center;
    font-family: "Cinzel", serif; font-weight: 500; font-size: 33px; letter-spacing: 10px; color: var(--ink);
  }
  .brand-rule {
    position: absolute; left: 90px; top: 527px; width: 436px; height: 6px; background: var(--leaf-green); border-radius: 3px;
  }
  .description {
    position: absolute; left: 30px; top: 570px; width: 520px;
    font-size: 15px; font-weight: 400; line-height: 25.5px; text-align: justify; color: #3a3935;
    hyphens: manual;
  }
  .net-weight {
    position: absolute; left: 570px; top: 720px;
    transform: rotate(-90deg); transform-origin: 0 0;
    font-size: 13px; font-weight: 600; letter-spacing: 1.5px; white-space: nowrap; color: var(--ink);
  }
</style>
</head>
<body>
  <section class="label">
    <div class="background-pattern" role="img" aria-label="Faint honey drip pattern in pale sage tones"></div>

    <p class="product-type">HEMP - INFUSED</p>
    <h2 class="product-name">HONEY</h2>

    <div class="farm-mark">
      <span class="farm-mark-square"></span>
      <span class="farm-mark-name">Tamsin Hollow Farm</span>
    </div>

    <div class="top-rule"></div>
    <p class="flavour">WILD FLOWER WITH RASBERRY</p>

    <h1 class="brand-name">TAMSIN</h1>
    <p class="brand-sub">HOLLOW FARM</p>
    <div class="brand-rule"></div>

    <p class="description">Lorem ipsum dolor sit amet, consectetuer adipiscing elit, sed diam nonummy nibh euismod tincidunt ut laoreet dolore magna aliquam erat volutpat. Ut wisi enim ad minim veniam, quis nos&shy;trud exerci tation ullamcorper suscipit lobortis nisl ut aliquip ex ea commodo consequat. Lorem ipsum dolor sit amet, consec&shy;tetuer adipiscing elit, sed diam nonummy nibh euismod tincid&shy;unt.</p>

    <p class="net-weight">NET WEIGHT&nbsp;&nbsp;(500 mg)</p>
  </section>
</body>
</html>
```